Forensic Psychology and Polygraph Needs Clever Catchy Logo

There's a massive trade show coming up and we are looking to debut a new, clever logo for our business cards. We are a private practice that offers psychological evaluations, therapeutic counseling, and polygraphing. Our website is ketvorin.com (to get a better idea of the color scheme) and instead of the nature/cuddly image that other psychology organizations like to go for, we are interested in cultivating a business, strength, and professional image.
Attached are some popular logos and designs to get those creative juices flowing! I would like to avoid the brain/psi logo as this has been to death so bonus points definitely for originality.
Target Market(s)
governmental agencies, third party mental health providers, individual private pay clients
Industry/Entity Type
Mental Health
Contact Information for Business Card
One one side will be the logo and company name while on the back will be contact information and provider details (name, position, etc)
Look and feel

```html
<!DOCTYPE html>
<html lang="en">
<head>
<meta charset="utf-8">
<title>Ketvorin &amp; Associates — Business Card</title>
<link href="https://fonts.googleapis.com/css2?family=Lato:wght@300;400;700&display=swap" rel="stylesheet">
<style>
  :root {
    --page: #1c1c1c;
    --card: #2b2b2b;
    --card-deep: #222222;
    --ink: #f4f4f4;
    --ink-soft: #8a8a8a;
    --photo-dark: #141414;
    --photo-mid: #3a3a3a;
  }
  * { margin: 0; padding: 0; box-sizing: border-box; }
  html, body { width: 1200px; height: 1200px; overflow: hidden; }
  body {
    background: var(--page);
    font-family: 'Lato', sans-serif;
    color: var(--ink);
    display: flex;
    flex-direction: column;
    align-items: center;
    justify-content: center;
    gap: 40px;
  }
  .card {
    position: relative;
    width: 940px;
    height: 537px;
    background: linear-gradient(135deg, var(--card) 0%, var(--card-deep) 100%);
    overflow: hidden;
    box-shadow: 0 18px 40px rgba(0,0,0,0.55);
  }
  .brand { position: absolute; }
  .brand-name {
    font-weight: 400;
    font-size: 46px;
    color: var(--ink);
    line-height: 1;
  }
  .brand-tag {
    font-weight: 300;
    font-size: 21px;
    letter-spacing: 0.42em;
    color: var(--ink-soft);
    margin-top: 8px;
    padding-left: 22px;
  }
  .card-front .brand { left: 250px; top: 222px; }

  .city-photo {
    position: absolute;
    inset: 0;
    width: 100%;
    height: 100%;
  }
  .card-back .brand { left: 36px; top: 340px; }
  .card-back .brand-name { font-size: 42px; }
  .card-back .brand-tag { font-size: 19px; }

  .provider {
    position: absolute;
    right: 40px;
    top: 56px;
    text-align: right;
  }
  .provider-name {
    font-weight: 400;
    font-size: 44px;
    letter-spacing: 0.06em;
    line-height: 1;
  }
  .provider-role {
    font-weight: 300;
    font-size: 19px;
    letter-spacing: 0.12em;
    color: var(--ink-soft);
    margin-top: 4px;
  }
  .contact {
    position: absolute;
    left: 560px;
    top: 250px;
    list-style: none;
  }
  .contact li {
    display: flex;
    align-items: flex-start;
    gap: 14px;
    font-size: 21px;
    font-weight: 400;
    line-height: 1.2;
    margin-bottom: 16px;
  }
  .contact .icon {
    flex: 0 0 32px;
    width: 32px;
    height: 32px;
  }
  .contact .address { line-height: 1.15; }
</style>
</head>
<body>

<section class="card card-front">
  <div class="brand">
    <div class="brand-name">Ketvorin &amp; Associates</div>
    <div class="brand-tag">Psychological Services</div>
  </div>
</section>

<section class="card card-back">
  <svg class="city-photo" viewBox="0 0 100 100" preserveAspectRatio="none" role="img" aria-label="Black and white photograph of a city skyline at night reflected in water">
    <defs>
      <linearGradient id="photoTone" x1="0" y1="0" x2="0" y2="1">
        <stop offset="0" stop-color="#303030"/>
        <stop offset="0.55" stop-color="#1b1b1b"/>
        <stop offset="1" stop-color="#0f0f0f"/>
      </linearGradient>
    </defs>
    <polygon points="0,20 34,20 58,56 38,100 0,100" fill="url(#photoTone)"/>
  </svg>

  <div class="brand">
    <div class="brand-name">Ketvorin &amp; Associates</div>
    <div class="brand-tag">Psychological Services</div>
  </div>

  <div class="provider">
    <div class="provider-name">DANA KETVORIN</div>
    <div class="provider-role">Licensed Psychologist</div>
  </div>

  <ul class="contact">
    <li>
      <svg class="icon" viewBox="0 0 32 32" aria-hidden="true">
        <circle cx="16" cy="16" r="16" fill="#f4f4f4"/>
        <path d="M11 9c1-.6 2 .2 2.6 1.6l.8 1.8c.3.8 0 1.4-.6 1.9l-.8.6c.8 1.8 2.1 3.1 3.9 3.9l.6-.8c.5-.6 1.1-.9 1.9-.6l1.8.8c1.4.6 2.2 1.6 1.6 2.6-.9 1.5-2.5 2.3-4.3 1.7-4-1.4-7.3-4.7-8.7-8.7-.6-1.8.2-3.4 1.2-4.8z" fill="#2b2b2b"/>
      </svg>
      <span>602 555 0148</span>
    </li>
    <li>
      <svg class="icon" viewBox="0 0 32 32" aria-hidden="true">
        <circle cx="16" cy="16" r="16" fill="#f4f4f4"/>
        <rect x="8" y="10.5" width="16" height="11" fill="none" stroke="#2b2b2b" stroke-width="1.8"/>
        <path d="M8 10.5l8 6.5 8-6.5" fill="none" stroke="#2b2b2b" stroke-width="1.8"/>
      </svg>
      <span>contact@ketvorin.com</span>
    </li>
    <li>
      <svg class="icon" viewBox="0 0 32 32" aria-hidden="true">
        <circle cx="16" cy="16" r="16" fill="#f4f4f4"/>
        <circle cx="16" cy="16" r="8" fill="none" stroke="#2b2b2b" stroke-width="1.8"/>
        <ellipse cx="16" cy="16" rx="3.5" ry="8" fill="none" stroke="#2b2b2b" stroke-width="1.4"/>
        <path d="M8 16h16" stroke="#2b2b2b" stroke-width="1.4"/>
      </svg>
      <span>www.ketvorin.com</span>
    </li>
    <li>
      <svg class="icon" viewBox="0 0 32 32" aria-hidden="true">
        <circle cx="16" cy="16" r="16" fill="#f4f4f4"/>
        <path d="M16 7a6 6 0 0 0-6 6c0 4.5 6 12 6 12s6-7.5 6-12a6 6 0 0 0-6-6z" fill="#2b2b2b"/>
        <circle cx="16" cy="13" r="2.2" fill="#f4f4f4"/>
      </svg>
      <span class="address">2280 W, Cedar Ridge Ave.<br>Suites 201 &amp; 204, Phoenix,<br>Arizona 85015</span>
    </li>
  </ul>
</section>

</body>
</html>
```